Wireless Broadband Newspaper AD

We have recently re-branded our company, new logo and website.

Our primary product offering is Wireless Broadband services to region, the target audience generally cannot get ADSL broadband.

We wanted to pose the question "Can't get ADSL ?" to attract the attention of those who are unable to access conventional mass market broadband offerings.

Ad Size should be:
129mm Wide
178mm High

Please find the text for the AD below.

Can't get ADSL ?
Try Fixed Wireless Broadband

* Speeds up to 10Mbit
* Plans from $29.95 per month
* Up to 60GB Download Allowance
* $99 Professional On-site Installation
* No Contracts

http://pelnetlink.com.au
CALL NOW - 1300 47 91 63

-

Target Market(s)

Frequent Internet users, requiring broadband access in their homes.

Industry/Entity Type

It Company

Requirements
Must have
• Ensure that the general branding feel of the existing website is considered, please us similar colours and theme.
• As well as our logo, which you will find attached in EPS format.
• http://pelnetlink.com.au
Nice to have
• Large caption "Can't get ADSL?"

```html
<!DOCTYPE html>
<html lang="en">
<head>
<meta charset="utf-8">
<title>Can't get ADSL? – Fixed Wireless Broadband</title>
<link rel="stylesheet" href="https://fonts.googleapis.com/css2?family=Audiowide&family=Noto+Sans:wght@400;700&display=swap">
<style>
  :root {
    --orange: #ff7a12;
    --orange-light: #ff9a2e;
    --white: #ffffff;
    --bg-dark: #2c2c2c;
    --bg-mid: #5a5a5a;
    --bg-light: #7a7a7a;
  }
  * { margin: 0; padding: 0; box-sizing: border-box; }
  html, body {
    width: 1200px;
    height: 900px;
    overflow: hidden;
    background: var(--bg-dark);
  }
  .ad {
    position: relative;
    width: 1200px;
    height: 900px;
    overflow: hidden;
    background: radial-gradient(ellipse 70% 65% at 62% 45%, var(--bg-light) 0%, var(--bg-mid) 40%, var(--bg-dark) 100%);
    font-family: "Noto Sans", Verdana, sans-serif;
    color: var(--white);
  }
  .globe-visual {
    position: absolute;
    left: 880px;
    top: 190px;
    width: 360px;
    height: 360px;
    border-radius: 50%;
    background: radial-gradient(circle at 40% 40%, rgba(140,190,200,0.55), rgba(70,110,120,0.35) 55%, rgba(60,60,60,0) 72%);
  }
  .cable-visual {
    position: absolute;
    left: 700px;
    top: 520px;
    width: 500px;
    height: 260px;
    background: radial-gradient(ellipse at 60% 40%, rgba(150,175,200,0.35), rgba(90,90,90,0) 70%);
  }
  .router-visual {
    position: absolute;
    left: 0;
    top: 510px;
    width: 670px;
    height: 390px;
    background: radial-gradient(ellipse 60% 45% at 45% 60%, #e6e6e6 0%, #bcbcbc 55%, rgba(90,90,90,0) 100%);
  }
  .headline {
    position: absolute;
    top: 36px;
    left: 0;
    width: 1200px;
    text-align: center;
    font-family: "Audiowide", sans-serif;
    font-size: 118px;
    line-height: 1;
    color: var(--orange);
    text-shadow: 0 4px 6px rgba(0,0,0,0.5);
  }
  .headline .question { color: var(--white); }
  .subhead {
    position: absolute;
    top: 188px;
    left: 0;
    width: 1200px;
    text-align: center;
    font-size: 44px;
    letter-spacing: 1px;
  }
  .features {
    position: absolute;
    top: 288px;
    left: 110px;
    list-style: none;
    font-size: 37px;
    letter-spacing: 1px;
    line-height: 47px;
    text-shadow: 0 2px 3px rgba(0,0,0,0.4);
  }
  .features li::before {
    content: "* ";
    color: var(--orange);
  }
  .features .highlight { color: var(--orange-light); }
  .brand {
    position: absolute;
    left: 830px;
    top: 600px;
    display: flex;
    align-items: center;
    gap: 14px;
    font-size: 46px;
    font-weight: 700;
    color: var(--white);
  }
  .brand-dot {
    width: 56px;
    height: 56px;
    border-radius: 50%;
    background: var(--orange);
  }
  .call-now {
    position: absolute;
    left: 820px;
    top: 732px;
    width: 280px;
    text-align: center;
    font-family: "Audiowide", sans-serif;
    font-size: 40px;
    color: var(--orange);
  }
  .phone {
    position: absolute;
    left: 730px;
    top: 784px;
    width: 380px;
    text-align: center;
    font-size: 50px;
    color: var(--white);
    letter-spacing: 1px;
  }
  .website {
    position: absolute;
    right: 14px;
    top: 852px;
    font-size: 30px;
    color: var(--orange);
  }
</style>
</head>
<body>
  <main class="ad">
    <div class="globe-visual" role="img" aria-label="Glowing globe of the earth"></div>
    <div class="cable-visual" role="img" aria-label="Network cable plugs"></div>
    <div class="router-visual" role="img" aria-label="White wireless broadband router with antenna"></div>

    <h1 class="headline">Can't get ADSL<span class="question">?</span></h1>
    <p class="subhead">Try Fixed Wireless Broadband</p>

    <ul class="features">
      <li>Speeds up to <span class="highlight">10Mbit</span></li>
      <li>Plans from <span class="highlight">$29.95</span> per month</li>
      <li>Up to <span class="highlight">60GB</span> Download Allowance</li>
      <li><span class="highlight">$99</span> Professional On-site Installation</li>
      <li>No Contracts</li>
    </ul>

    <div class="brand"><span class="brand-dot"></span>pelnetlink</div>

    <p class="call-now">CALL NOW</p>
    <p class="phone">1300 47 91 63</p>
    <p class="website">http://pelnetlink.com.au</p>
  </main>
</body>
</html>
```